brisk-vale.com Real Estate, Investment, Financial corporate

Real Estate, Investment, Financial corporate looking site. Show present a professional firm, with an elegant display. Please see the attached file which includes the logo, palette and fonts.
Updates

We just starting the brief today. ( logo was delayed)

Target Market(s)

Investors, Corporate , B2b

Industry/Entity Type

real-estate investments

Number of Pages Required

3 page

Requirements
Must have
• Dazzling Homepage
Nice to have
• paralex

```html
<!DOCTYPE html>
<html lang="en">
<head>
<meta charset="utf-8">
<title>brisk-vale.com — Real Estate</title>
<link rel="stylesheet" href="https://fonts.googleapis.com/css2?family=Nunito:wght@300;400;600;700&display=swap">
<style>
:root{
  --pink:#e55fd3;
  --ink:#111;
  --text:#222;
  --muted:#777;
  --light:#a9a9a9;
  --line:#e8e8e8;
  --footer:#f8f8f8;
  --black:#000;
}
*{margin:0;padding:0;box-sizing:border-box}
html,body{width:1200px;height:5164px;overflow:hidden}
body{position:relative;background:#fff;font-family:'Nunito',sans-serif;color:var(--text)}
.abs{position:absolute}
p{font-size:12px;line-height:22px;color:var(--muted)}

/* header */
.brand{left:118px;top:32px;font-size:15px;font-weight:700;color:var(--ink);z-index:3}
.nav{right:144px;top:34px;display:flex;gap:30px;font-size:12px;z-index:3}
.nav a{color:var(--ink);text-decoration:none}
.nav a.active{color:var(--pink)}

/* hero */
.hero{left:0;top:0;width:1200px;height:662px;
  background:linear-gradient(180deg,#fafbfd 0%,#e8ecf2 40%,#d6dbe2 70%,#b9bec6 100%);
  clip-path:polygon(0 0,100% 0,100% 612px,50% 662px,0 612px)}
.hero-title{left:0;top:238px;width:1200px;text-align:center;font-size:46px;font-weight:300;line-height:52px;color:var(--ink)}
.hero-sub{left:290px;top:362px;width:620px;text-align:center;font-size:13px;line-height:22px;color:#333}
.scroll-dot{left:568px;top:614px;width:64px;height:64px;border-radius:50%;background:var(--pink);display:flex;align-items:center;justify-content:center}

/* section heads */
.eyebrow{left:0;width:1200px;text-align:center;font-size:9px;letter-spacing:2px;color:var(--pink);font-weight:600}
.eyebrow span{display:inline-block;width:36px;height:1px;background:var(--pink);vertical-align:middle;margin:0 10px}
.heading{left:0;width:1200px;text-align:center;font-size:30px;font-weight:400;color:var(--ink)}

/* services */
.service{top:850px;width:240px;text-align:center}
.service svg{display:block;margin:0 auto 30px}
.service h3{font-size:17px;font-weight:400;color:var(--ink);margin-bottom:10px}

/* offers */
.offer{top:1238px;width:302px;height:320px}
.offer .photo{width:302px;height:196px}
.offer .body{position:absolute;left:24px;top:158px;width:216px;height:162px;background:#fff;padding:18px 12px}
.price{font-size:12px;color:var(--ink)}
.price s{color:var(--muted);margin-right:14px}
.price small{color:var(--light);font-size:9px}
.meta{font-size:11px;color:var(--muted);margin-top:14px}
.offer h4{font-size:13px;font-weight:400;color:var(--ink);margin-top:16px}
.offer .city{font-size:11px;color:var(--muted);margin-top:12px}
.offer .go{position:absolute;right:-30px;bottom:-4px;width:32px;height:32px;background:var(--pink);display:flex;align-items:center;justify-content:center}

/* workflow */
.flow{left:38px;top:1674px;width:562px;height:752px;background:var(--black);clip-path:polygon(0 0,100% 0,100% 100%,0 94.6%)}
.flow-photo{left:600px;top:1674px;width:562px;height:752px;
  background:linear-gradient(160deg,#c9c6c2 0%,#9c9690 40%,#5a4f46 75%,#3a302a 100%);
  clip-path:polygon(0 0,100% 0,100% 94.6%,0 100%)}
.flow-eyebrow{left:38px;top:1756px;width:562px;text-align:center;font-size:9px;letter-spacing:2px;color:#fff;font-weight:600}
.flow-eyebrow span{display:inline-block;width:36px;height:1px;background:#fff;vertical-align:middle;margin:0 10px}
.flow-title{left:38px;top:1776px;width:562px;text-align:center;font-size:28px;color:#fff}
.step{width:230px;text-align:center}
.step .num{width:66px;height:66px;border-radius:50%;background:var(--pink);color:#fff;font-size:22px;margin:0 auto 16px;display:flex;align-items:center;justify-content:center;border:3px solid #fff}
.step h3{font-size:17px;font-weight:400;color:#fff;margin-bottom:8px}
.step p{color:#ccc}

/* about */
.about-photo{left:124px;top:2512px;width:476px;height:440px;background:linear-gradient(180deg,#e9cfc6 0%,#c8a99c 45%,#5d524d 100%)}
.about-card{left:508px;top:2550px;width:560px;height:364px;background:#fff;padding:50px 36px}
.about-card h2{font-size:28px;font-weight:400;color:var(--ink);margin-bottom:22px}
.about-card p{font-size:11px;margin-bottom:14px}
.stat{top:2988px;display:flex;align-items:center;gap:12px;height:56px;padding-right:50px;border-right:1px solid var(--line)}
.stat b{font-size:36px;font-weight:400;color:var(--ink)}
.stat span{font-size:11px;color:var(--muted);line-height:15px}

/* testimonials */
.quote{top:3308px;width:290px;padding:0 16px}
.quote .who{display:flex;align-items:center;gap:14px;margin-top:26px}
.avatar{width:56px;height:56px;border-radius:50%;background:linear-gradient(135deg,#d8d8d8,#7a7a7a)}
.who b{display:block;font-size:14px;font-weight:400;color:var(--ink)}
.who i{font-style:normal;font-size:10px;color:var(--light)}
.dots{left:0;top:3510px;width:1200px;display:flex;justify-content:center;gap:8px}
.dots i{width:7px;height:7px;border-radius:50%;background:#ddd}
.dots i:first-child{background:var(--pink)}

/* agents */
.agent-photo{left:124px;top:3720px;width:220px;height:280px;background:linear-gradient(180deg,#f3f3f3 0%,#dde3ea 60%,#c7ccd3 100%)}
.agent-card{left:136px;top:3964px;width:184px;height:66px;background:#fff;padding:12px 18px}
.agent-card b{display:block;font-size:15px;font-weight:400;color:var(--ink)}
.agent-card span{font-size:11px;color:var(--muted)}
.agent-card em{font-style:normal;color:var(--ink)}

/* blog */
.post{top:4262px;width:222px}
.post h4{font-size:13px;font-weight:400;color:var(--ink);line-height:20px}
.post .date{font-size:8px;letter-spacing:1px;color:var(--light);margin-top:4px}
.post .img{width:222px;height:156px;margin-top:14px}
.post p{font-size:11px;margin-top:18px}

/* footer */
.footer{left:0;top:4682px;width:1200px;height:482px;background:var(--footer)}
.fcol{top:4776px}
.fcol h5{font-size:14px;font-weight:400;color:var(--ink);margin-bottom:34px}
.fcol ul{list-style:none}
.fcol li{font-size:11px;color:#555;line-height:22px}
.fcol li::before{content:"→";color:var(--pink);margin-right:6px}
.contact-row{display:flex;gap:18px;font-size:11px;color:#555;line-height:18px;margin-bottom:22px}
.contact-row.pink span{color:var(--pink)}
.social{left:134px;top:4944px;display:flex;gap:36px}
.social i{width:14px;height:14px;border-radius:50%;background:var(--pink)}
.copy{left:0;top:5036px;width:1200px;text-align:center;font-size:11px;color:#555}
</style>
</head>
<body>

<div class="abs hero" role="img" aria-label="Row of white residential villas with red roofs and a parked car under a pale sky"></div>
<div class="abs brand">brisk-vale.com</div>
<nav class="abs nav"><a class="active" href="#">Home</a><a href="#">Services</a><a href="#">Contact</a></nav>
<h1 class="abs hero-title">The Simplest<br>Way to Find Property</h1>
<div class="abs hero-sub">A small river named Duden flows by their place and supplies it with the necessary regelialia. It is a paradisematic country, in which roasted parts</div>
<div class="abs scroll-dot"><svg width="14" height="14" viewBox="0 0 14 14"><path d="M7 1v10M3 7l4 4 4-4" stroke="#fff" stroke-width="1.5" fill="none"/></svg></div>

<!-- services -->
<div class="abs eyebrow" style="top:744px"><span></span>OUR SERVICES<span></span></div>
<h2 class="abs heading" style="top:762px">The smartest way to buy a home</h2>

<div class="abs service" style="left:114px">
  <svg width="52" height="52" viewBox="0 0 52 52" fill="none" stroke="#e55fd3" stroke-width="1.4"><ellipse cx="26" cy="30" rx="18" ry="13"/><circle cx="34" cy="14" r="7"/><path d="M14 40v6M36 40v6M8 28H4"/></svg>
  <h3>No Downpayment</h3><p>A small river named Duden flows by their place and supplies it with the necessary regelialia.</p>
</div>
<div class="abs service" style="left:358px">
  <svg width="52" height="52" viewBox="0 0 52 52" fill="none" stroke="#e55fd3" stroke-width="1.4"><rect x="6" y="14" width="40" height="30" rx="3"/><path d="M10 14l22-8 4 8"/><rect x="32" y="24" width="14" height="10"/><circle cx="38" cy="29" r="2"/></svg>
  <h3>All Cash Offer</h3><p>A small river named Duden flows by their place and supplies it with the necessary regelialia.</p>
</div>
<div class="abs service" style="left:602px">
  <svg width="52" height="52" viewBox="0 0 52 52" fill="none" stroke="#e55fd3" stroke-width="1.4"><rect x="12" y="6" width="28" height="40"/><path d="M18 16h16M18 22h16M18 28h16M18 34h10"/></svg>
  <h3>Experts in Your Corner</h3><p>A small river named Duden flows by their place and supplies it with the necessary regelialia.</p>
</div>
<div class="abs service" style="left:846px">
  <svg width="52" height="52" viewBox="0 0 52 52" fill="none" stroke="#e55fd3" stroke-width="1.4"><rect x="12" y="22" width="28" height="24"/><path d="M18 22v-8a8 8 0 0 1 16 0v8"/><path d="M26 30v8"/></svg>
  <h3>Lokced in Pricing</h3><p>A small river named Duden flows by their place and supplies it with the necessary regelialia.</p>
</div>

<!-- offers -->
<div class="abs eyebrow" style="top:1132px"><span></span>WHAT WE OFFER<span></span></div>
<h2 class="abs heading" style="top:1150px">Exclusive Offer For You</h2>

<div class="abs offer" style="left:124px">
  <div class="photo" role="img" aria-label="Bright living room with sofa and open kitchen" style="background:linear-gradient(160deg,#e9e6e2,#b8aea4)"></div>
  <div class="body"><div class="price"><s>800,000</s>$3,050<small>/mo</small></div><div class="meta">▭ 3 &nbsp; ⌒ 2 &nbsp; ▣ 1,878 sqft</div><h4>The Blue Sky Home</h4><div class="city">Oakland</div>
  <div class="go"><svg width="12" height="12" viewBox="0 0 12 12" fill="none" stroke="#fff" stroke-width="1.3"><path d="M5 7l2-2M4 5L2 7a2 2 0 0 0 3 3l2-2M8 7l2-2a2 2 0 0 0-3-3L5 4"/></svg></div></div>
</div>
<div class="abs offer" style="left:448px">
  <div class="photo" role="img" aria-label="Modern white kitchen with dining table" style="background:linear-gradient(160deg,#efece7,#c4bbb2)"></div>
  <div class="body"><div class="price"><s>800,000</s>$3,050<small>/mo</small></div><div class="meta">▭ 3 &nbsp; ⌒ 2 &nbsp; ▣ 1,878 sqft</div><h4>The Blue Sky Home</h4><div class="city">Oakland</div>
  <div class="go"><svg width="12" height="12" viewBox="0 0 12 12" fill="none" stroke="#fff" stroke-width="1.3"><path d="M5 7l2-2M4 5L2 7a2 2 0 0 0 3 3l2-2M8 7l2-2a2 2 0 0 0-3-3L5 4"/></svg></div></div>
</div>
<div class="abs offer" style="left:774px">
  <div class="photo" role="img" aria-label="White hallway with wooden staircase" style="background:linear-gradient(160deg,#f2f2f2,#bdb3a8)"></div>
  <div class="body"><div class="price"><s>800,000</s>$3,050<small>/mo</small></div><div class="meta">▭ 3 &nbsp; ⌒ 2 &nbsp; ▣ 1,878 sqft</div><h4>The Blue Sky Home</h4><div class="city">Oakland</div>
  <div class="go"><svg width="12" height="12" viewBox="0 0 12 12" fill="none" stroke="#fff" stroke-width="1.3"><path d="M5 7l2-2M4 5L2 7a2 2 0 0 0 3 3l2-2M8 7l2-2a2 2 0 0 0-3-3L5 4"/></svg></div></div>
</div>

<!-- workflow -->
<div class="abs flow"></div>
<div class="abs flow-photo" role="img" aria-label="Living room with stone fireplace, sofa and dark wood floor"></div>
<div class="abs flow-eyebrow"><span></span>WORK FLOW<span></span></div>
<h2 class="abs flow-title">How it works</h2>
<div class="abs step" style="left:118px;top:1886px"><div class="num">01</div><h3>Evaluate Property</h3><p>A small river named Duden flows by their place and supplies it with the necessary regelialia.</p></div>
<div class="abs step" style="left:362px;top:1886px"><div class="num">02</div><h3>Meet Your Agent</h3><p>A small river named Duden flows by their place and supplies it with the necessary regelialia.</p></div>
<div class="abs step" style="left:118px;top:2108px"><div class="num">03</div><h3>Close the Deal</h3><p>A small river named Duden flows by their place and supplies it with the necessary regelialia.</p></div>
<div class="abs step" style="left:362px;top:2108px"><div class="num">04</div><h3>Have Your Property</h3><p>A small river named Duden flows by their place and supplies it with the necessary regelialia.</p></div>

<!-- about -->
<div class="abs about-photo" role="img" aria-label="Group of friends beside an off-road vehicle at sunset"></div>
<div class="abs about-card">
  <h2>We Put People First.</h2>
  <p>A small river named Duden flows by their place and supplies it with the necessary regelialia. It is a paradisematic country, in which roasted parts of sentences fly into your mouth.</p>
  <p>On her way she met a copy. The copy warned the Little Blind Text, that where it came from it would have been rewritten a thousand times and everything that was left from its origin would be the word "and" and the Little Blind Text should turn around and return to its own, safe country. But nothing the copy said could convince her and so it didn't take long until a few insidious Copy Writers ambushed her, made her drunk with Longe and Parole and dragged her into their agency, where they abused her for their.</p>
</div>
<div class="abs stat" style="left:124px"><b>305</b><span>Area<br>Population</span></div>
<div class="abs stat" style="left:370px"><b>1,090</b><span>Total<br>Properties</span></div>

<!-- testimonials -->
<div class="abs quote" style="left:124px"><p>Far far away, behind the word mountains, far from the countries Vokalia and Consonantia, there live the blind texts.</p><div class="who"><div class="avatar" role="img" aria-label="Portrait of client"></div><div><b>Dana Merrow</b><i>Marketing Manager</i></div></div></div>
<div class="abs quote" style="left:448px"><p>Far far away, behind the word mountains, far from the countries Vokalia and Consonantia, there live the blind texts.</p><div class="who"><div class="avatar" role="img" aria-label="Portrait of client"></div><div><b>Dana Merrow</b><i>Marketing Manager</i></div></div></div>
<div class="abs quote" style="left:774px"><p>Far far away, behind the word mountains, far from the countries Vokalia and Consonantia, there live the blind texts.</p><div class="who"><div class="avatar" role="img" aria-label="Portrait of client"></div><div><b>Dana Merrow</b><i>Marketing Manager</i></div></div></div>
<div class="abs dots"><i></i><i></i><i></i><i></i><i></i></div>

<!-- agents -->
<div class="abs eyebrow" style="top:3604px"><span></span>AGENTS<span></span></div>
<h2 class="abs heading" style="top:3622px">Our Agents</h2>
<div class="abs agent-photo" role="img" aria-label="Smiling agent holding a small model house"></div>
<div class="abs agent-card"><b>Owen Hartley</b><span>Listing — <em>10 Properties</em></span></div>

<!-- blog -->
<div class="abs eyebrow" style="top:4150px"><span></span>BLOG<span></span></div>
<h2 class="abs heading" style="top:4168px">Recent Blog</h2>
<div class="abs post" style="left:124px"><h4>Why Lead Generation is Key for Business Growth</h4><div class="date">JULY 24, 2019 &nbsp;ADMIN &nbsp;▪ 3</div><div class="img" role="img" aria-label="Bathroom with freestanding tub" style="background:linear-gradient(160deg,#c8bdb3,#7a6a5e)"></div><p>A small river named Duden flows by their place and supplies it with the necessary regelialia.</p></div>
<div class="abs post" style="left:368px"><h4>Why Lead Generation is Key for Business Growth</h4><div class="date">JULY 24, 2019 &nbsp;ADMIN &nbsp;▪ 3</div><div class="img" role="img" aria-label="Empty modern interior with large windows" style="background:linear-gradient(160deg,#6c7680,#3b4148)"></div><p>A small river named Duden flows by their place and supplies it with the necessary regelialia.</p></div>
<div class="abs post" style="left:612px"><h4>Why Lead Generation is Key for Business Growth</h4><div class="date">JULY 24, 2019 &nbsp;ADMIN &nbsp;▪ 3</div><div class="img" role="img" aria-label="Shelved room with white doorway" style="background:linear-gradient(160deg,#e8e2da,#9b7d64)"></div><p>A small river named Duden flows by their place and supplies it with the necessary regelialia.</p></div>
<div class="abs post" style="left:856px"><h4>Why Lead Generation is Key for Business Growth</h4><div class="date">JULY 24, 2019 &nbsp;ADMIN &nbsp;▪ 3</div><div class="img" role="img" aria-label="Warmly lit room with hanging lights" style="background:linear-gradient(160deg,#e3b58a,#5a3a26)"></div><p>A small river named Duden flows by their place and supplies it with the necessary regelialia.</p></div>

<!-- footer -->
<footer class="abs footer"></footer>
<div class="abs fcol" style="left:124px;width:170px"><h5>Uptown</h5><p style="font-size:11px;color:#555">Far far away, behind the word mountains, far from the countries.</p></div>
<div class="abs social"><i></i><i></i></div>
<div class="abs fcol" style="left:336px"><h5>Community</h5><ul><li>Search Properties</li><li>For Agents</li><li>Reviews</li><li>FAQs</li></ul></div>
<div class="abs fcol" style="left:532px"><h5>About Us</h5><ul><li>Our Story</li><li>Meet the team</li><li>Careers</li></ul></div>
<div class="abs fcol" style="left:708px"><h5>Company</h5><ul><li>About Us</li><li>Press</li><li>Contact</li><li>Careers</li></ul></div>
<div class="abs fcol" style="left:904px;width:190px"><h5>Have a Questions?</h5>
  <div class="contact-row"><svg width="10" height="14" viewBox="0 0 10 14"><path d="M5 0a5 5 0 0 0-5 5c0 4 5 9 5 9s5-5 5-9a5 5 0 0 0-5-5z" fill="#e55fd3"/><circle cx="5" cy="5" r="2" fill="#fff"/></svg><span>48 Alder Row, Fenwick, Oregon, USA</span></div>
  <div class="contact-row pink"><svg width="12" height="12" viewBox="0 0 12 12"><path d="M2 1l3 1-1 2 4 4 2-1 1 3-2 1C5 11 1 7 1 3z" fill="#e55fd3"/></svg><span>+1 555 0142 870</span></div>
  <div class="contact-row pink"><svg width="12" height="10" viewBox="0 0 12 10"><rect width="12" height="10" fill="#e55fd3"/><path d="M0 0l6 5 6-5" stroke="#fff" fill="none"/></svg><span>hello@brisk-vale.com</span></div>
</div>
<div class="abs copy">Copyright © 2021 All rights reserved | brisk-vale.com</div>

</body>
</html>
```